Chat Software Business Card Design

We need a business card design for our company.

We provide businesses with a platform to communicate with their web visitors in real time using chat boxes on their web sites.

We're using a bright color scheme to attract attention on the site and the business card would do well to reflect this also to maintain brand awareness. However it is not essential to the ultimate design to use the same color scheme or feel as the site.

We offer a Free Trial of the software and would encourage a business card design to promote this if possible.

http://qelmarworks7.co.uk/projects/guest/index2.html

You will find the company logo attached also.

An eye catching design with something that will set the card apart from others is required.

The design of the card/theme of the card should be very unique, setting our selves apart, eye catching whilst not providing a "wacky" image for the company.

It should also include our contact information;~
Website - www.talkpond-live.com
Email - support@talkpond-live.com
Twitter - @Talkpondlive

Industry/Entity Type

Software

Contact Information for Business Card

Web - www.talkpond-live.com
Email - office@talkpond-live.com
Skype - Talkpond.Live

Requirements
Must have
• Use of company logo is required.

```html
<!DOCTYPE html>
<html lang="en">
<head>
<meta charset="utf-8">
<title>Talkpond Live – Business Card</title>
<link href="https://fonts.googleapis.com/css2?family=Open+Sans:wght@300;600;700;800&display=swap" rel="stylesheet">
<style>
  :root {
    --sky: #18a9e4;
    --sky-light: #47bdf0;
    --sky-deep: #0f93cf;
    --bubble: #ffffff;
    --bubble-edge: #c9d3da;
    --ink: #1b1b1b;
    --brand-orange: #e8532b;
    --page: #ffffff;
  }
  * { box-sizing: border-box; margin: 0; padding: 0; }
  html, body { width: 1200px; height: 960px; overflow: hidden; background: var(--page); }
  body { font-family: "Open Sans", Arial, sans-serif; color: var(--ink); }

  .sheet {
    width: 1200px; height: 960px;
    display: flex; flex-direction: column; align-items: center; justify-content: center;
    gap: 60px;
  }
  .card {
    position: relative; width: 700px; height: 400px;
    border-radius: 6px; overflow: hidden;
    box-shadow: 0 6px 20px rgba(0,0,0,0.15);
  }
  .card-pattern {
    position: absolute; inset: 0;
    background: linear-gradient(160deg, var(--sky-light) 0%, var(--sky) 45%, var(--sky-deep) 100%);
  }
  .card-shapes { position: absolute; inset: 0; width: 700px; height: 400px; }
  .bubble-shape { fill: var(--bubble); stroke: var(--bubble-edge); stroke-width: 3; }

  /* front */
  .front-brand {
    position: absolute; left: 120px; top: 40px;
    font-weight: 800; font-size: 84px; line-height: 0.95; color: #ffffff;
    letter-spacing: -1px;
  }
  .front-brand .second-line { display: block; padding-left: 230px; }
  .tagline {
    position: absolute; left: 70px; top: 262px; width: 530px; text-align: center;
  }
  .tagline-main { font-weight: 700; font-size: 25px; letter-spacing: 0.5px; }
  .tagline-offer { font-weight: 300; font-size: 24px; margin-top: 2px; letter-spacing: 0.5px; }

  /* back */
  .back-brand {
    position: absolute; left: 30px; top: 60px; width: 300px; height: 110px;
    display: flex; align-items: center; justify-content: center;
    font-weight: 800; font-size: 40px; color: var(--brand-orange); letter-spacing: -0.5px;
  }
  .contact-list {
    position: absolute; left: 352px; top: 182px; list-style: none;
    font-weight: 600; font-size: 17px; line-height: 27px;
  }
  .contact-list li { display: flex; align-items: center; gap: 12px; }
  .contact-icon { width: 18px; height: 18px; flex: none; }
  .contact-icon .stroke { fill: none; stroke: var(--ink); stroke-width: 1.6; }
  .contact-icon .dot { fill: var(--ink); }
</style>
</head>
<body>
<main class="sheet">

  <section class="card card-back" aria-label="Card back with contact details">
    <div class="card-pattern" role="img" aria-label="Soft blue sky background with faint clouds"></div>
    <svg class="card-shapes" viewBox="0 0 700 400" aria-hidden="true">
      <path class="bubble-shape" d="M48 60 H312 Q330 60 330 78 V152 Q330 170 312 170 H110 L62 212 L78 170 H48 Q30 170 30 152 V78 Q30 60 48 60 Z"/>
      <path class="bubble-shape" d="M350 168 H642 Q660 168 660 186 V314 Q660 332 642 332 H400 L352 368 L366 332 H350 Q332 332 332 314 V186 Q332 168 350 168 Z"/>
    </svg>
    <div class="back-brand">Talkpond Live</div>
    <ul class="contact-list">
      <li>
        <svg class="contact-icon" viewBox="0 0 18 18" aria-hidden="true"><rect class="stroke" x="1.5" y="2.5" width="15" height="10" rx="1"/><path class="stroke" d="M6 16 H12 M9 12.5 V16"/></svg>
        www.talkpond-live.com
      </li>
      <li>
        <svg class="contact-icon" viewBox="0 0 18 18" aria-hidden="true"><rect class="stroke" x="1.5" y="4" width="15" height="10"/><path class="stroke" d="M1.5 4 L9 10 L16.5 4"/></svg>
        office@talkpond-live.com
      </li>
      <li>
        <svg class="contact-icon" viewBox="0 0 18 18" aria-hidden="true"><rect class="stroke" x="1.5" y="4" width="15" height="10"/><path class="stroke" d="M1.5 4 L9 10 L16.5 4"/></svg>
        support@talkpond-live.com
      </li>
      <li>
        <svg class="contact-icon" viewBox="0 0 18 18" aria-hidden="true"><circle class="dot" cx="9" cy="9" r="7"/></svg>
        @Talkpondlive
      </li>
      <li>
        <svg class="contact-icon" viewBox="0 0 18 18" aria-hidden="true"><circle class="dot" cx="9" cy="9" r="7"/></svg>
        Talkpond.Live
      </li>
    </ul>
  </section>

  <section class="card card-front" aria-label="Card front with brand and free trial offer">
    <div class="card-pattern" role="img" aria-label="Blue background with a faint repeating chat bubble pattern"></div>
    <svg class="card-shapes" viewBox="0 0 700 400" aria-hidden="true">
      <path class="bubble-shape" d="M92 248 H580 Q602 248 602 270 V322 Q602 344 580 344 H560 L574 384 L520 344 H92 Q70 344 70 322 V270 Q70 248 92 248 Z"/>
    </svg>
    <div class="front-brand">Talkpond<span class="second-line">Live</span></div>
    <div class="tagline">
      <p class="tagline-main">Because Your Customer Matters!</p>
      <p class="tagline-offer">Take advantage of our free trial</p>
    </div>
  </section>

</main>
</body>
</html>
```